Redesign MuseQuill's Artist Profile Page

MuseQuill is a contemporary arts website that has a large worldwide community of artists with profile pages for each artist showing artwork, exhibits, bio data, etc.

For an example please see: http://www.musequill-example.com/global/artists/show/47302-dorian-pell

We would like a slight redesign on these pages within the context of the current website. We are interested in modernizing and lightening the design. The artwork should be the primary focus.

Target Market(s)

Professional artists, galleries and collectors

Industry/Entity Type

Artists

Requirements
Must have
• All the current functionality on the page.

```html
<!DOCTYPE html>
<html lang="en">
<head>
<meta charset="utf-8">
<title>MuseQuill Worldwide – Artist Profile</title>
<link rel="stylesheet" href="https://fonts.googleapis.com/css2?family=Arimo:wght@400;700&family=Yanone+Kaffeesatz:wght@400;500&display=swap">
<style>
:root{
  --olive:#7f8a17;
  --ink:#333;
  --grey-text:#555;
  --muted:#777;
  --label-grey:#8a8a8a;
  --tab:#dcdcdc;
  --tab-line:#c8c8c8;
  --panel:#efefef;
  --frame:#e2e2e2;
  --footer:#dedede;
  --sky:#5a86c4;
}
*{box-sizing:border-box;margin:0;padding:0}
html,body{width:1200px;height:766px;overflow:hidden;background:#fff}
body{position:relative;font-family:"Arimo",Arial,sans-serif;color:var(--ink)}
.abs{position:absolute}

.brand{left:14px;top:20px;font-family:"Arimo",Arial,sans-serif;font-weight:700;font-size:46px;color:var(--olive);letter-spacing:-1px;line-height:1;white-space:nowrap}
.section-label{left:14px;top:82px;font-family:"Arimo",Arial,sans-serif;font-size:29px;color:var(--label-grey);line-height:1}
.cities{right:14px;top:16px;text-align:right;font-size:13px;line-height:17px;color:var(--olive)}
.cities span{color:var(--muted);padding:0 2px}

.main-nav{left:212px;top:86px;display:flex;gap:4px}
.tab{width:105px;height:34px;border-radius:6px 6px 0 0;background:linear-gradient(#ececec,var(--tab));border:1px solid var(--tab-line);border-bottom:none;font-size:15px;color:#333;display:flex;align-items:center;justify-content:center}
.tab.active{background:var(--olive);border-color:var(--olive);color:#fff}
.nav-rule{left:0;top:120px;width:1200px;height:3px;background:#cfcfcf}

.sub-nav{right:14px;top:137px;font-size:14px;color:#222}
.sub-nav span{padding:0 3px;color:#555}

.heading{font-family:"Yanone Kaffeesatz",sans-serif;font-weight:500;color:var(--olive);font-size:29px;line-height:1}
.statement-title{left:22px;top:152px}
.statement{left:19px;top:193px;width:522px;font-size:13px;line-height:21.6px;text-align:justify;color:#222}

.facts{left:12px;top:304px;width:538px;height:126px;border:5px solid var(--panel);border-radius:4px}
.facts-title{left:28px;top:290px;background:#fff;padding:0 10px 0 4px}
.fact{font-size:14px}
.fact b{color:#444}

.actions-title{left:14px;top:446px}
.actions{left:15px;top:484px;list-style:none;font-size:14px;color:var(--muted)}
.actions li{height:21.6px;display:flex;align-items:center;gap:9px}
.actions svg{width:13px;height:13px;flex:none}

.share-btn{left:13px;top:646px;height:23px;padding:0 8px;border:1px solid #bbb;border-radius:3px;background:linear-gradient(#fff,#e6e6e6);font-size:13px;font-weight:700;color:#333;display:flex;align-items:center}
.share-count{left:89px;top:646px;width:18px;height:23px;border:1px solid #bbb;font-size:12px;display:flex;align-items:center;justify-content:center;background:#fff}
.save-btn{left:123px;top:646px;width:56px;height:25px;border:1px solid #b6c2d8;border-radius:3px;background:#eef1f8;font-size:13px;color:#3b5998;display:flex;align-items:center;justify-content:center}

.news-title{left:262px;top:446px}
.news{left:260px;width:289px;height:80px;background:var(--panel);padding:7px 6px;font-size:14px;line-height:21.6px;color:var(--grey-text)}

.viewer{left:563px;top:158px;width:624px;height:420px;border:1px solid var(--frame)}
.artwork{left:576px;top:172px;width:599px;height:393px;background:linear-gradient(160deg,#7da3d6 0%,var(--sky) 45%,#b9cbe2 70%,#3c3630 100%)}
.strip{left:563px;top:585px;width:624px;height:100px;border:1px solid var(--frame)}
.thumb{top:594px;width:84px;height:84px;background:linear-gradient(#a9b3bd,#6b6560)}

.footer{left:0;top:694px;width:1200px;height:72px;background:var(--footer);box-shadow:inset 0 6px 6px -4px rgba(0,0,0,.18)}
.copyright{right:10px;top:708px;font-size:13px;color:#555}
.counter{right:12px;top:740px;font-size:13px;color:#555}
</style>
</head>
<body>
<header>
  <div class="abs brand">MuseQuill Worldwide</div>
  <div class="abs section-label">Profile</div>
  <div class="abs cities">Chicago <span>|</span> Los Angeles <span>|</span> Miami <span>|</span> New York <span>|</span> San Francisco <span>|</span> Santa Fe<br>Amsterdam <span>|</span> Berlin <span>|</span> Brussels <span>|</span> London <span>|</span> Paris <span>|</span> China <span>|</span> India <span>|</span> Worldwide</div>
  <nav class="abs main-nav">
    <div class="tab active">Home</div><div class="tab">Magazine</div><div class="tab">Calendar</div><div class="tab">Galleries</div><div class="tab">Art</div><div class="tab">Shop</div><div class="tab">Artists</div><div class="tab">Community</div><div class="tab">Add</div>
  </nav>
  <div class="abs nav-rule"></div>
</header>

<nav class="abs sub-nav">Profile <span>|</span> Artworks <span>|</span> For Sale <span>|</span> Network <span>|</span> Reviews <span>|</span> Comments</nav>

<h2 class="abs heading statement-title">Statement</h2>
<p class="abs statement">Dorian Pell lives and works in and around Paris.&nbsp; His photography has been shown in all kinds of small galleries, clubs, and alternative arts spaces.&nbsp; He is particularly interested in creating a documentation of people in ordinary, everyday activities, looking for the moments of beauty or magic in the quotidien.</p>

<div class="abs facts"></div>
<h2 class="abs heading facts-title">Quick Facts</h2>
<div class="abs fact" style="left:40px;top:346px"><b>Birth Place</b></div>
<div class="abs fact" style="left:149px;top:346px">Paris</div>
<div class="abs fact" style="left:268px;top:346px"><b>Lives in</b></div>
<div class="abs fact" style="left:365px;top:346px">Paris</div>
<div class="abs fact" style="left:40px;top:380px"><b>Birth Year</b></div>
<div class="abs fact" style="left:149px;top:380px">1974</div>
<div class="abs fact" style="left:268px;top:380px"><b>Works in</b></div>
<div class="abs fact" style="left:365px;top:380px">Paris</div>

<h2 class="abs heading actions-title">Actions</h2>
<ul class="abs actions">
  <li><svg viewBox="0 0 13 13"><circle cx="6.5" cy="6.5" r="5.5" fill="none" stroke="#8a9a1a" stroke-width="1.5"/><path d="M6.5 3.5v6M3.5 6.5h6" stroke="#8a9a1a" stroke-width="1.5"/></svg>Add to my list</li>
  <li><svg viewBox="0 0 13 13"><rect x="1" y="1" width="11" height="11" fill="#f3e9a8" stroke="#777"/><path d="M4 10l2.5-6 2.5 6z" fill="#555"/></svg>View a large slideshow</li>
  <li><svg viewBox="0 0 13 13"><rect x="1" y="2.5" width="11" height="8" fill="#f6efc4" stroke="#888"/><path d="M1 2.5l5.5 4.5 5.5-4.5" fill="none" stroke="#888"/></svg>Email this Artist</li>
  <li><svg viewBox="0 0 13 13"><path d="M6.5 1l6 11h-12z" fill="#e8861c"/><path d="M6.5 5v3.5" stroke="#fff" stroke-width="1.5"/><circle cx="6.5" cy="10.2" r=".8" fill="#fff"/></svg>Report Abuse</li>
  <li><svg viewBox="0 0 13 13"><circle cx="6.5" cy="6.5" r="5.5" fill="none" stroke="#999" stroke-width="1.3"/><text x="6.5" y="9.8" font-size="9" text-anchor="middle" fill="#888" font-family="Arimo,sans-serif">?</text></svg>Contact us for help</li>
  <li><svg viewBox="0 0 13 13"><rect x="1.5" y="2" width="10" height="9" rx="1.5" fill="#cfcfcf"/></svg>Bookmark this</li>
  <li><svg viewBox="0 0 13 13"><circle cx="6.5" cy="6.5" r="5.5" fill="#3b9a3b"/></svg>Discover it!</li>
</ul>
<div class="abs share-btn">Share</div>
<div class="abs share-count">0</div>
<div class="abs save-btn">Save</div>

<h2 class="abs heading news-title">News &amp; Buzz</h2>
<div class="abs news" style="top:476px">Upcoming Harborline Special Editions<br>Mara Vellin : On our worldwode watchlist<br>Watchlist Artist : Tobin Reyes</div>
<div class="abs news" style="top:564px">Upcoming Harborline Special Editions<br>Mara Vellin : On our worldwode watchlist<br>Watchlist Artist : Tobin Reyes</div>

<div class="abs viewer"></div>
<div class="abs artwork" role="img" aria-label="Featured photograph: looking up through a dark window frame at blue sky and clouds"></div>
<div class="abs strip"></div>
<svg class="abs" style="left:572px;top:629px" width="8" height="12" viewBox="0 0 8 12"><path d="M7 0v12L0 6z" fill="var(--olive)"/></svg>
<svg class="abs" style="left:1168px;top:629px" width="8" height="12" viewBox="0 0 8 12"><path d="M1 0v12l7-6z" fill="var(--olive)"/></svg>
<div class="abs thumb" style="left:594px" role="img" aria-label="Thumbnail photograph of a person outdoors"></div>
<div class="abs thumb" style="left:690px;background:linear-gradient(#cfcac4,#4a4540)" role="img" aria-label="Thumbnail photograph of a person in a hat"></div>
<div class="abs thumb" style="left:786px;background:linear-gradient(#9aa0a6,#2f2a28)" role="img" aria-label="Thumbnail photograph of a person at a market"></div>
<div class="abs thumb" style="left:882px;background:linear-gradient(#c99a90,#5a3550)" role="img" aria-label="Thumbnail photograph of a person in a purple scarf"></div>
<div class="abs thumb" style="left:978px;background:linear-gradient(#d8d8d8,#6a625c)" role="img" aria-label="Thumbnail photograph of a person in sunglasses"></div>
<div class="abs thumb" style="left:1074px;background:linear-gradient(#c7c3bc,#4e4640)" role="img" aria-label="Thumbnail photograph of a person on a street"></div>

<footer>
  <div class="abs footer"></div>
  <div class="abs copyright">© 2012 MuseQuill Worldwide. All Rights Reserved.</div>
  <div class="abs counter">X 30</div>
</footer>
</body>
</html>
```